Updated Business Card for Optometry Practice

We're a growing optometry practice that is moving to a beautiful new office and we want to update our business card. We just updated our logo so the new card should reflect the new logo. Our practice continually invests in state of the art instruments to help us provide eye care that is thorough, comfortable, efficient and educational.

I've attached our current card and logo. You can reference this for the information I would like on the card. The tag line on the back is "Clear vision for every family."

Upon completion of this project we will need (amongst other formats) Photoshop files of the card so I can change employee names to print cards for each employee.

```html
<!DOCTYPE html>
<html lang="en">
<head>
<meta charset="utf-8">
<title>Brightwell Family Eyecare – Business Card</title>
<link rel="stylesheet" href="https://fonts.googleapis.com/css2?family=Montserrat:wght@400;500;600;700&display=swap">
<style>
  :root {
    --stage: #737373;
    --navy: #13294f;
    --gold: #d4ad2c;
    --white: #ffffff;
    --ink: #1f2a44;
    --rule: #c9c9c9;
  }
  * { box-sizing: border-box; margin: 0; padding: 0; }
  html, body {
    width: 1200px; height: 1000px; overflow: hidden;
    background: var(--stage);
    font-family: "Montserrat", sans-serif;
  }
  .card {
    position: absolute;
    width: 613px; height: 351px;
    border-radius: 22px;
    overflow: hidden;
  }
  .card-front { left: 293px; top: 113px; background: var(--navy); }
  .card-back { left: 292px; top: 505px; background: var(--white); }

  .brand {
    position: absolute;
    font-weight: 600;
    letter-spacing: 0.04em;
    line-height: 1;
    text-transform: uppercase;
  }
  .brand .brand-main { display: block; font-size: 38px; }
  .brand .brand-sub { display: block; font-size: 15px; letter-spacing: 0.22em; margin-top: 10px; }
  .card-front .brand { left: 52px; top: 143px; color: var(--white); }
  .card-back .brand { left: 0; right: 0; top: 48px; text-align: center; color: var(--navy); }
  .card-back .brand .brand-main { font-size: 30px; }
  .card-back .brand .brand-sub { font-size: 12px; margin-top: 8px; }

  .tagline {
    position: absolute; left: 69px; top: 228px;
    color: var(--white); font-size: 13px; font-weight: 400;
  }

  .person {
    position: absolute; right: 345px; top: 176px; text-align: right;
  }
  .person-name { color: var(--navy); font-weight: 700; font-size: 17px; }
  .person-role { color: var(--gold); font-weight: 500; font-size: 15px; margin-top: 2px; }

  .contacts {
    position: absolute; left: 308px; top: 170px; list-style: none;
  }
  .contacts li {
    display: flex; align-items: center; gap: 12px;
    font-size: 13.5px; color: var(--ink); height: 17px;
  }
  .contacts svg { width: 15px; height: 15px; fill: var(--gold); flex: none; }

  .divider {
    position: absolute; left: 71px; width: 477px; top: 265px;
    height: 1px; background: var(--rule);
  }
  .office {
    position: absolute; left: 0; right: 0; top: 290px; text-align: center;
  }
  .office-name { color: var(--gold); font-weight: 600; font-size: 13px; }
  .office-address { color: var(--ink); font-size: 13.5px; margin-top: 2px; }
</style>
</head>
<body>

<section class="card card-front">
  <div class="brand">
    <span class="brand-main">Brightwell</span>
    <span class="brand-sub">Family Eyecare</span>
  </div>
  <p class="tagline">Clear vision for every family</p>
</section>

<section class="card card-back">
  <div class="brand">
    <span class="brand-main">Brightwell</span>
    <span class="brand-sub">Family Eyecare</span>
  </div>

  <div class="person">
    <p class="person-name">Daniel Corwin, OD</p>
    <p class="person-role">Optometrist</p>
  </div>

  <ul class="contacts">
    <li>
      <svg viewBox="0 0 24 24" aria-hidden="true"><path d="M6.6 10.8a15.1 15.1 0 0 0 6.6 6.6l2.2-2.2a1 1 0 0 1 1-.25 11.4 11.4 0 0 0 3.6.57 1 1 0 0 1 1 1V20a1 1 0 0 1-1 1A17 17 0 0 1 3 4a1 1 0 0 1 1-1h3.5a1 1 0 0 1 1 1c0 1.25.2 2.45.57 3.57a1 1 0 0 1-.25 1z"/></svg>
      (555) 214-7830
    </li>
    <li>
      <svg viewBox="0 0 24 24" aria-hidden="true"><path d="M2 5h20v14H2z M2 5l10 7 10-7" stroke="#fff" stroke-width="1.6"/></svg>
      dan@brightwellfamilyeyecare.com
    </li>
    <li>
      <svg viewBox="0 0 24 24" aria-hidden="true"><circle cx="12" cy="12" r="10"/><path d="M2 12h20M12 2c3 3 3 17 0 20M12 2c-3 3-3 17 0 20M4 7h16M4 17h16" stroke="#fff" stroke-width="1.3" fill="none"/></svg>
      brightwellfamilyeyecare.com
    </li>
  </ul>

  <div class="divider"></div>

  <div class="office">
    <p class="office-name">Brightwell Family Eyecare</p>
    <p class="office-address">2810 Harmon Ridge Blvd #104, Brightwell, MO 63300</p>
  </div>
</section>

</body>
</html>
```